Flyer Needed for Westland Advocacy Summit 2017

We need a flyer designed for a save the date for Verdant Goods Forum in California on August 23, 2017. The lobby day is taking place in Sacramento so please design the flyer using these details.

Requirements
Must have
• - Date must be clear
Nice to have
• - Must have "save the date"
• - Something that catches your eye

```html
<!DOCTYPE html>
<html lang="en">
<head>
<meta charset="utf-8">
<title>Save the Date – Verdant Goods Forum in California</title>
<link href="https://fonts.googleapis.com/css2?family=Great+Vibes&family=Raleway:wght@400&family=Vollkorn:wght@700&family=Montserrat:wght@800&display=swap" rel="stylesheet">
<style>
  :root {
    --ink-brown: #3b2420;
    --script-brown: #4a2a28;
    --leaf-green: #4f8f3a;
    --vine-green: #6e9a55;
    --banner-orange: #e78a24;
    --dot-orange: #e07f22;
    --sea-deep: #5db6c7;
    --sea-light: #bfe2e4;
    --foam: #f3f4f1;
    --sand: #e4d5c1;
    --sand-dark: #d9c7af;
  }
  * { margin: 0; padding: 0; box-sizing: border-box; }
  html, body { width: 927px; height: 1200px; overflow: hidden; }
  body { position: relative; background: var(--sand); }

  .beach-scene {
    position: absolute; inset: 0;
    background:
      radial-gradient(ellipse 200px 170px at 548px 728px, rgba(120,70,25,.55), rgba(120,70,25,0) 100%),
      linear-gradient(180deg,
        var(--sea-deep) 0%, var(--sea-light) 10%, var(--foam) 20%,
        #eceeec 33%, #e9dfd0 38%, var(--sand) 48%, var(--sand-dark) 100%);
  }

  .leaf-sprig {
    position: absolute; top: 36px; width: 160px; height: 150px;
    background: radial-gradient(ellipse at center, rgba(79,143,58,.45), rgba(79,143,58,0) 70%);
  }
  .leaf-sprig.left { left: 215px; }
  .leaf-sprig.right { left: 580px; }

  .heading { position: absolute; left: 0; right: 0; text-align: center; }
  .save-script {
    top: 72px;
    font-family: "Great Vibes", cursive; font-weight: 400;
    font-size: 124px; line-height: 1;
    color: var(--script-brown);
  }
  .the-date {
    top: 214px;
    font-family: "Raleway", sans-serif; font-weight: 400;
    font-size: 58px; letter-spacing: 27px; padding-left: 27px;
    color: var(--leaf-green); line-height: 1;
  }

  .star-row { position: absolute; top: 296px; left: 384px; }

  .event-banner { position: absolute; left: 0; top: 0; }
  .event-title {
    position: absolute; left: 463px; top: 491px;
    transform: translate(-50%, -50%) rotate(-12.7deg);
    white-space: nowrap; text-align: center;
    font-family: "Vollkorn", serif; font-weight: 700;
    font-size: 44px; letter-spacing: 4px; line-height: 62px;
    color: var(--ink-brown); text-transform: uppercase;
  }

  .flourish {
    position: absolute; top: 938px; width: 136px; height: 34px;
    background: radial-gradient(ellipse at center, rgba(110,154,85,.45), rgba(110,154,85,0) 70%);
  }
  .flourish.left { left: 303px; }
  .flourish.right { left: 488px; }

  .event-date {
    position: absolute; left: 0; right: 0; top: 994px;
    text-align: center;
    font-family: "Montserrat", sans-serif; font-weight: 800;
    font-size: 49px; line-height: 62px; letter-spacing: 4px;
    color: var(--ink-brown);
  }
  .date-dot {
    position: absolute; top: 1066px; width: 6px; height: 6px;
    border-radius: 50%; background: var(--dot-orange);
  }
</style>
</head>
<body>
  <div class="beach-scene" role="img" aria-label="Photo of a coconut lying on sandy beach with ocean waves behind"></div>

  <span class="leaf-sprig left" role="img" aria-label="Green leaf sprig ornament"></span>
  <span class="leaf-sprig right" role="img" aria-label="Green leaf sprig ornament"></span>

  <h1 class="heading save-script">Save</h1>
  <h2 class="heading the-date">THE DATE</h2>

  <svg class="star-row" width="190" height="44" viewBox="0 0 190 44" aria-hidden="true">
    <g fill="#3b2420">
      <polygon points="22,2 27,16 42,16 30,25 34,40 22,31 10,40 14,25 2,16 17,16"/>
      <polygon points="95,2 100,16 115,16 103,25 107,40 95,31 83,40 87,25 75,16 90,16"/>
      <polygon points="168,2 173,16 188,16 176,25 180,40 168,31 156,40 160,25 148,16 163,16"/>
    </g>
  </svg>

  <svg class="event-banner" width="927" height="1200" viewBox="0 0 927 1200" aria-hidden="true">
    <polygon points="105,485 822,323 822,498 105,660" fill="#e78a24"/>
  </svg>
  <div class="event-title">Verdant Goods Forum<br>in California</div>

  <span class="flourish left" role="img" aria-label="Green vine flourish ornament"></span>
  <span class="flourish right" role="img" aria-label="Green vine flourish ornament"></span>

  <p class="event-date">AUGUST 23<br>2017</p>
  <span class="date-dot" style="left:320px"></span>
  <span class="date-dot" style="left:601px"></span>
</body>
</html>
```